Plumber referral program cards

We're a busy Restoration company servicing residential and commercial properties damaged by water fire and mold. We hold the standard for Excellence, Integrity and Reliability.
This business card needs to be designed to generate high quality plumbing leads through water damage referrals

FRONT: (no specific chronological order)
-Water Damage Referral program for plumbers
-We pay plumbers $800 CASH on each water damage referral everyday!
-"To us, business is personal. Which is why referrals means rewards."
-Refer and Earn• Paid same day!

- Your customer will ALWAYS receive a FREE evaluation.
Rapid Response
24 hours a day/7 days a week

BACK: (no specific chronological order)
Water extraction•plumbing leaks•slab leaks•
Sub floor drying and repairs•Sewage cleanup•supply line rupture •structural drying•overflows•mold remediation•

-Call Zen Oak next time you run into a water damage!
515-7-ZEN-OAK

Elite Plumber Referral Program Bonuses
-Just to show how much your referrals mean to us, Receive $100 on every referral sent, No matter what!
- Refer Zen Oak to other property service professionals, and you recieve $100 cash for every job THEY send us!

Contact us for more information
RB Morlan
Water Damage Restoration Specialist
Phone: 515-7-ZENOAK
Email: Rmorlan@callzenoak.com
Website: www.callzenoak.com

Plumbers

Rapid Response

515-7-ZEN-OAK

RB Morlan
Phone: 515-7-ZENOAK

• Times etc

• Emphasized $800 referral fee
• Eye catching & appealing
• Our company logo and color matching
• Attached files of example competitors ads

```html
<!DOCTYPE html>
<html lang="en">
<head>
<meta charset="utf-8">
<title>Zen Oak – Plumber Referral Cards</title>
<link href="https://fonts.googleapis.com/css2?family=Roboto+Condensed:wght@400;700;900&family=Tinos:ital,wght@0,400;0,700;1,400;1,700&display=swap" rel="stylesheet">
<style>
  :root{
    --navy:#0d2f6e;
    --blue:#1f5fb8;
    --sky:#5aa8e6;
    --ice:#e6f3fc;
    --red:#d3202a;
    --white:#ffffff;
    --stage:#e9e7e3;
    --ink:#1a2a4a;
  }
  *{box-sizing:border-box;margin:0;padding:0}
  html,body{width:900px;height:1200px;overflow:hidden;background:var(--stage)}
  body{position:relative;font-family:"Tinos","Times New Roman",serif;color:var(--ink)}
  .card{position:absolute;left:50px;width:800px;height:460px;background:var(--white);border-radius:16px;overflow:hidden;box-shadow:0 4px 14px rgba(0,0,0,.18)}
  .card--front{top:120px}
  .card--back{top:620px}
  .band{position:absolute;left:0;right:0;display:flex;align-items:center;justify-content:center;text-align:center}

  /* front */
  .water-top{position:absolute;left:0;top:0;width:100%;height:150px;background:linear-gradient(180deg,#0f3f8f 0%,#2d7dd0 55%,#9fd0f2 100%)}
  .brand{top:0;height:150px;gap:14px;color:var(--white)}
  .brand__mark{width:26px;height:26px;border-radius:50%;background:var(--white);flex:none}
  .brand__name{font-family:"Tinos",serif;font-weight:700;font-size:52px;line-height:1}
  .program{top:150px;height:28px;color:var(--navy);font-family:"Roboto Condensed",sans-serif;font-weight:700;font-size:19px;letter-spacing:.5px;border-top:2px solid var(--navy)}
  .offer{top:178px;height:74px;background:var(--red);color:var(--white);flex-direction:column;font-family:"Roboto Condensed",sans-serif}
  .offer__main{font-size:44px;font-weight:900;line-height:1}
  .offer__sub{font-size:19px;font-weight:700;margin-top:4px}
  .quote{top:258px;height:56px;flex-direction:column;color:var(--navy);font-style:italic;font-size:17px;line-height:1.3}
  .evaluation{top:318px;height:30px;background:var(--blue);color:var(--white);font-size:16px}
  .water-bottom{position:absolute;left:0;bottom:0;width:100%;height:112px;background:linear-gradient(180deg,#f4fbff 0%,#b9def6 55%,#4d97d8 100%)}
  .response{top:360px;height:80px;flex-direction:column;color:var(--navy);font-family:"Roboto Condensed",sans-serif;font-weight:700}
  .response__label{font-size:18px;letter-spacing:1px}
  .response__hours{font-size:26px;letter-spacing:.5px}

  /* back */
  .services{position:absolute;left:0;top:0;width:100%;height:132px;background:linear-gradient(180deg,#0f3f8f 0%,#2468c2 70%,#7fbde9 100%);display:grid;grid-template-columns:repeat(3,1fr);padding:22px 40px 0 60px;color:var(--white);font-size:17px}
  .services ul{list-style:none}
  .services li{line-height:1.5}
  .services li::before{content:"\2666";font-size:12px;margin-right:8px;vertical-align:2px}
  .call{top:140px;height:34px;color:var(--blue);font-family:"Roboto Condensed",sans-serif;font-weight:900;font-size:26px}
  .phone-big{top:174px;height:38px;color:var(--red);font-family:"Roboto Condensed",sans-serif;font-weight:900;font-size:34px;letter-spacing:1px}
  .bonus-title{top:218px;height:28px;background:var(--red);color:var(--white);font-style:italic;font-weight:700;font-size:18px}
  .bonus-text{top:250px;height:72px;flex-direction:column;color:var(--navy);font-style:italic;font-size:15px;line-height:1.35;padding:0 60px}
  .contact-title{top:324px;height:28px;background:var(--blue);color:var(--white);font-family:"Roboto Condensed",sans-serif;font-weight:700;font-size:18px;letter-spacing:1px}
  .contact{position:absolute;top:356px;left:0;right:0;height:64px;display:flex;align-items:center;justify-content:center;gap:70px}
  .person__name{font-size:26px;font-weight:700;color:var(--navy)}
  .person__role{font-size:16px;color:var(--red)}
  .details{list-style:none;font-size:16px;color:var(--navy)}
  .details li{display:flex;align-items:center;gap:8px;line-height:1.5}
  .details svg{width:16px;height:16px;flex:none}
  .site-strip{position:absolute;left:0;bottom:0;width:100%;height:40px;background:linear-gradient(180deg,#9fd0f2 0%,#2d7dd0 100%)}
  .website{bottom:0;height:40px;color:var(--white);font-weight:700;font-size:17px;letter-spacing:.5px}
</style>
</head>
<body>

<section class="card card--front">
  <div class="water-top" role="img" aria-label="Blue water splash background"></div>
  <div class="band brand">
    <span class="brand__mark"></span>
    <span class="brand__name">Zen Oak</span>
  </div>
  <div class="band program">WATER DAMAGE REFERRAL PROGRAM FOR PLUMBERS</div>
  <div class="band offer">
    <div class="offer__main">WE PAY PLUMBERS $800 CASH</div>
    <div class="offer__sub">ON EACH WATER DAMAGE REFERRAL EVERYDAY!</div>
  </div>
  <div class="band quote">
    <p>"To us, business is personal. Which is why referrals means rewards."</p>
    <p>Refer and Earn • Paid same day!</p>
  </div>
  <div class="band evaluation">Your customer will ALWAYS receive a FREE evaluation.</div>
  <div class="water-bottom" role="img" aria-label="Light water splash background"></div>
  <div class="band response">
    <div class="response__label">RAPID RESPONSE</div>
    <div class="response__hours">24 HOURS A DAY/7 DAYS A WEEK</div>
  </div>
</section>

<section class="card card--back">
  <div class="services">
    <ul><li>Water extraction</li><li>Plumbing leaks</li><li>Slab leaks</li></ul>
    <ul><li>Sub floor drying and repairs</li><li>Sewage cleanup</li><li>Supply line ruptures</li></ul>
    <ul><li>Structural drying</li><li>Overflows</li><li>Mold remediation</li></ul>
  </div>
  <div class="band call">CALL ZEN OAK NEXT TIME YOU RUN INTO A WATER DAMAGE!</div>
  <div class="band phone-big">515-7-ZEN-OAK</div>
  <div class="band bonus-title">Elite Plumber Referral Program Bonuses</div>
  <div class="band bonus-text">
    <p>Just to show how much your referrals mean to us, Receive $100 on every referral sent, No matter what!</p>
    <p>Refer Zen Oak to other property service professionals, and you recieve $100 cash for every job THEY send us!</p>
  </div>
  <div class="band contact-title">CONTACT US FOR MORE INFORMATION</div>
  <div class="contact">
    <div class="person">
      <div class="person__name">RB Morlan</div>
      <div class="person__role">Water Damage Restoration Specialist</div>
    </div>
    <ul class="details">
      <li><svg viewBox="0 0 16 16"><rect width="16" height="16" rx="3" fill="#d3202a"/><path d="M5 3.5l1.6 2.2-1 1.1a6 6 0 0 0 3.6 3.6l1.1-1 2.2 1.6-.8 1.5c-4.4-.2-7.8-3.6-8-8z" fill="#fff"/></svg>515-7-ZENOAK</li>
      <li><svg viewBox="0 0 16 16"><rect width="16" height="16" rx="3" fill="#d3202a"/><rect x="3" y="4.5" width="10" height="7" fill="none" stroke="#fff" stroke-width="1.3"/><path d="M3 4.5l5 4 5-4" fill="none" stroke="#fff" stroke-width="1.3"/></svg>Rmorlan@callzenoak.com</li>
    </ul>
  </div>
  <div class="site-strip" role="img" aria-label="Water splash strip"></div>
  <div class="band website">www.callzenoak.com</div>
</section>

</body>
</html>
```